Plumbing Products Website

This project is to create a web page for Mr. Clear Brook and Mr. Hot Kettle's product offerings. There are 14 unique products. The main page will showcase all 14 products arranged in a clean, concise format that flows nicely and is easy to read.
Furthermore, I need a unique page for each of the 14 products that the main page can link the products to so visitors can click each of them to "Learn More".
For reference, our websites are MrBrookly.example and TopBoilerHub.example; so keep the branding, color-scheme, header, footer, etc. consistent with MrBrookly.example and TopBoilerHub.example.
For reference, here is the catalog. Feel free to copy as much of the content as necessary to build the pages:
https://catalogs.pagefolio.example/MrHotKettle/qvtx/
For clarification, the products are:
1. Whole House Water Purification System
2. Whole House Water Ionization System
3. Whole House Water Softener System
4. Water Heater Sediment Pre-Filter
5. Whole-House UV Water Sterilization System
6. The ULTIMATE Whole House Water Treatment System
7. Under-Sink Reverse Osmosis System with UV Sterilizer
8. Smart Water Heater Regulator with Automated Stand-By for Power Savings
9. Whole House Water Pressure Booster
10. Hot Water Heater Tank Volume Booster
11. Leak Detector with Automatic Water Shutoff
12. Whole House UV Air Purification System
13. Leak Detector Alarm with Mobile App
14. Multi-Gas Detector for Carbon Monoxide, Natural Gas, Propane, Methane, Explosive Gasses, Smoke & Fire
Unfortunately, all the content was created by AI, so I don't have any "original" images or other media. I have attached the logos for your reference though. Also, each individual catalog page is attached.
Once the winning design is chosen, I will need the pages coded and hosted on a staging server for me to view in a live environment before I move them to my server.
Let me know if you have any questions.

```html
<!DOCTYPE html>
<html lang="en">
<head>
<meta charset="utf-8">
<title>Our Solutions – Mr. Clear Brook</title>
<link href="https://fonts.googleapis.com/css2?family=Inter:wght@400;500;600;700;800&family=Bebas+Neue&display=swap" rel="stylesheet">
<style>
:root{
  --navy:#0a2a78;
  --navy-deep:#0b2468;
  --blue:#0e47b8;
  --link:#0f3fa8;
  --teal:#17b3c4;
  --sky:#1b8fd8;
  --gold:#f7c623;
  --ink:#1f2430;
  --muted:#6b7280;
  --card-shadow:0 4px 18px rgba(20,40,90,.10);
}
*{box-sizing:border-box;margin:0;padding:0}
html,body{width:1200px;height:2410px;overflow:hidden}
body{font-family:"Inter",sans-serif;color:var(--ink);background:#fff;position:relative}
.topbar{height:41px;background:linear-gradient(90deg,var(--sky),var(--teal));display:flex;justify-content:flex-end;align-items:center;gap:30px;padding-right:124px;color:#fff;font-size:12px;white-space:nowrap}
.topbar span{display:flex;align-items:center;gap:8px}
.topbar .ic{width:18px;height:18px;border-radius:50%;background:#fff;display:grid;place-items:center}
.nav{height:103px;display:flex;align-items:center;padding:0 124px 0 125px;white-space:nowrap}
.brand{display:flex;align-items:center;gap:8px;font-weight:800;font-size:15px;color:var(--navy);flex:0 0 auto}
.brand .dot{width:22px;height:22px;border-radius:50%;background:var(--blue)}
.menu{display:flex;gap:44px;margin-left:auto;margin-right:39px;font-size:13px}
.menu a{color:var(--ink);text-decoration:none;position:relative;white-space:nowrap}
.menu a.active{color:var(--blue)}
.menu a.active::after{content:"";position:absolute;left:12px;right:12px;bottom:-9px;height:2px;background:var(--blue)}
.btn{flex:0 0 auto;white-space:nowrap;background:var(--navy);color:#fff;font-weight:600;font-size:13px;height:45px;border-radius:4px;display:flex;align-items:center;gap:14px;padding:0 6px 0 14px}
.btn .sq{width:33px;height:33px;background:#fff;border-radius:3px;display:grid;place-items:center}
.hero{position:relative;height:462px;background:linear-gradient(100deg,#0b2f86 0%,#123d9a 55%,#1b5fb0 100%);overflow:hidden;color:#fff}
.hero-photo{position:absolute;right:0;top:0;width:520px;height:100%;background:linear-gradient(90deg,rgba(18,61,154,0),#3a6a8a 30%,#6f8d7a 70%,#4f7c5c)}
.promo{position:absolute;left:127px;top:33px;border:1px solid #5aa6ff;padding:7px 48px 7px 22px;font-size:16px;font-weight:500;letter-spacing:.3px;white-space:nowrap}
.promo::after{content:"";position:absolute;right:14px;top:9px;width:16px;height:16px;border-radius:50%;background:var(--gold)}
.hero h1{position:absolute;left:127px;top:78px;font-family:"Bebas Neue",sans-serif;font-weight:400;font-size:46px;letter-spacing:.2px;white-space:nowrap}
.special{position:absolute;left:127px;top:136px;width:454px;height:137px;border:1px solid #4a8fe8;background:rgba(10,40,120,.35)}
.special .lbl{position:absolute;left:22px;top:8px;font-family:"Bebas Neue",sans-serif;font-size:38px;color:var(--gold)}
.special .price{position:absolute;left:20px;top:38px;font-family:"Bebas Neue",sans-serif;font-size:92px;color:var(--gold);line-height:1}
.special .price sup{font-size:46px;vertical-align:26px}
.special .inst{position:absolute;left:183px;top:50px;font-weight:800;font-size:40px;white-space:nowrap}
.special .reg{position:absolute;left:183px;top:98px;font-weight:700;font-size:17px;white-space:nowrap}
.tagline{position:absolute;left:133px;top:286px;font-size:12px;font-weight:500;white-space:nowrap}
.feats{position:absolute;left:133px;top:318px;display:flex;gap:10px;font-size:11px;font-weight:600;line-height:13px;white-space:nowrap}
.feats div{display:flex;align-items:center;gap:5px}
.feats i{width:30px;height:30px;border-radius:50%;border:1.5px solid #6fb6ff;display:inline-block}
.seal{position:absolute;left:758px;top:308px;width:122px;height:122px;border-radius:50%;background:#0b2468;border:3px solid #5aa6ff;text-align:center;font-weight:800;font-size:12px;line-height:14px;padding-top:20px}
.seal b{display:block;font-family:"Bebas Neue",sans-serif;font-weight:400;font-size:42px;line-height:40px;color:var(--gold)}
.solutions{text-align:center;padding-top:66px}
.solutions h2{font-size:34px;font-weight:700}
.solutions p{margin:14px auto 0;width:440px;font-size:15px;line-height:25px;color:var(--muted)}
.grid{position:absolute;left:125px;top:803px;width:949px;display:grid;grid-template-columns:repeat(4,222px);column-gap:20px;row-gap:34px}
.card{position:relative;height:319px;background:#fff;box-shadow:var(--card-shadow);border-radius:3px}
.card .shot{position:absolute;left:14px;top:30px;right:14px;height:190px;background:radial-gradient(circle at 50% 55%,#cfdcf2,#f3f6fb 70%)}
.card h3{position:absolute;left:13px;right:4px;top:240px;font-size:15px;font-weight:600;line-height:18.5px;letter-spacing:-.15px;color:var(--link)}
.go{position:absolute;right:0;top:0;width:45px;height:45px;background:linear-gradient(135deg,var(--sky),var(--teal));display:grid;place-items:center;border-radius:0 3px 0 0}
.card.wide{position:absolute;left:368px;top:1860px;width:463px;height:215px}
.card.wide .shot{left:50px;top:30px;width:140px;height:155px;background:linear-gradient(180deg,#2a2a2a,#e68a2a 45%,#2a2a2a)}
.card.wide h3{left:193px;top:80px;width:230px;right:auto}
footer{position:absolute;left:0;top:2142px;width:1200px;height:268px;background:var(--navy-deep);color:#fff}
.f-brand{position:absolute;left:125px;top:40px;font-weight:800;font-size:17px;display:flex;align-items:center;gap:8px}
.f-brand .dot{width:24px;height:24px;border-radius:50%;background:var(--sky)}
.f-about{position:absolute;left:125px;top:123px;width:215px;font-size:10.5px;line-height:13px;color:#9fb0d6}
.socials{position:absolute;left:125px;top:187px;display:flex;gap:12px}
.socials i{width:25px;height:25px;border-radius:50%;background:#fff;display:block}
.col{position:absolute;top:48px;font-size:11px;color:#9fb0d6;white-space:nowrap}
.col h4{font-size:13px;font-weight:500;color:#fff;margin-bottom:13px}
.col li{list-style:none;margin-bottom:10px;display:flex;gap:7px;align-items:center}
.bottom{position:absolute;left:0;bottom:0;width:100%;height:25px;background:#0a1f5a;text-align:center;font-size:11px;line-height:25px;color:#9fb0d6}
</style>
</head>
<body>
<div class="topbar">
  <span><i class="ic"><svg width="10" height="10" viewBox="0 0 24 24"><path fill="#1b8fd8" d="M6.6 10.8a15 15 0 0 0 6.6 6.6l2.2-2.2c.3-.3.7-.4 1-.2 1.1.4 2.3.6 3.6.6.6 0 1 .4 1 1V20c0 .6-.4 1-1 1A17 17 0 0 1 3 4c0-.6.4-1 1-1h3.5c.6 0 1 .4 1 1 0 1.3.2 2.5.6 3.6.1.3 0 .7-.2 1z"/></svg></i>555-210-4480</span>
  <span><i class="ic"><svg width="10" height="10" viewBox="0 0 24 24"><path fill="#1b8fd8" d="M3 5h18v14H3zm2 2v.5l7 4.5 7-4.5V7z"/></svg></i>info@topboilerhub.example</span>
</div>
<header class="nav">
  <div class="brand"><span class="dot"></span>Mr. Clear Brook</div>
  <nav class="menu"><a href="#">Home</a><a href="#" class="active">Products</a><a href="#">About Us</a><a href="#">Resources</a><a href="#">Support</a><a href="#">Contact Us</a></nav>
  <a class="btn">Schedule Install <span class="sq"><svg width="14" height="14" viewBox="0 0 14 14"><path d="M3 11 11 3M5 3h6v6" stroke="#0a2a78" stroke-width="1.5" fill="none"/></svg></span></a>
</header>
<section class="hero">
  <div class="hero-photo" role="img" aria-label="Whole-house filter housing on copper pipes in front of a modern home"></div>
  <div class="promo">LIMITED-TIME SUMMER PROMOTION</div>
  <h1>WHOLE-HOUSE WATER PURIFICATION SYSTEM</h1>
  <div class="special">
    <div class="lbl">SUMMER SPECIAL:</div>
    <div class="price"><sup>$</sup>995</div>
    <div class="inst">INSTALLED!</div>
    <div class="reg">Regular Price $1500</div>
  </div>
  <div class="tagline">Cleaner, better tasting water at every tap — professionally installed for one low summer price.</div>
  <div class="feats">
    <div><i></i>Reduces Rust,<br>Bacteria &amp; Scale</div>
    <div><i></i>Protects Pipes, Fixtures<br>&amp; Household Systems</div>
    <div><i></i>Healthier<br>Skin &amp; Hair</div>
    <div><i></i>Provides Cleaner, Softer,<br>Better Tasting Water</div>
  </div>
  <div class="seal">REMOVES<br>UP TO<b>99.9%</b>OF IMPURITIES!</div>
</section>
<section class="solutions">
  <h2>Our 13 Solutions</h2>
  <p>Explore our complete range of water treatment, water heating and home safety products</p>
</section>
<div class="grid">
  <article class="card"><div class="shot" role="img" aria-label="Triple blue filter purification rack"></div><a class="go"><svg width="18" height="18" viewBox="0 0 14 14"><path d="M3 11 11 3M5 3h6v6" stroke="#fff" stroke-width="1.4" fill="none"/></svg></a><h3>Whole House Water Purification System</h3></article>
  <article class="card"><div class="shot" role="img" aria-label="Water ionizer unit with filters"></div><a class="go"><svg width="18" height="18" viewBox="0 0 14 14"><path d="M3 11 11 3M5 3h6v6" stroke="#fff" stroke-width="1.4" fill="none"/></svg></a><h3>Whole House Water Ionization System</h3></article>
  <article class="card"><div class="shot" role="img" aria-label="Twin softener tanks with brine tank"></div><a class="go"><svg width="18" height="18" viewBox="0 0 14 14"><path d="M3 11 11 3M5 3h6v6" stroke="#fff" stroke-width="1.4" fill="none"/></svg></a><h3>Whole House Water Softener System</h3></article>
  <article class="card"><div class="shot" role="img" aria-label="Sediment pre-filter housing"></div><a class="go"><svg width="18" height="18" viewBox="0 0 14 14"><path d="M3 11 11 3M5 3h6v6" stroke="#fff" stroke-width="1.4" fill="none"/></svg></a><h3>Water Heater Sediment Pre-Filter</h3></article>
  <article class="card"><div class="shot" role="img" aria-label="Stainless UV sterilization chamber"></div><a class="go"><svg width="18" height="18" viewBox="0 0 14 14"><path d="M3 11 11 3M5 3h6v6" stroke="#fff" stroke-width="1.4" fill="none"/></svg></a><h3>Whole-House UV Water Sterilization System</h3></article>
  <article class="card"><div class="shot" role="img" aria-label="Complete multi-stage treatment setup"></div><a class="go"><svg width="18" height="18" viewBox="0 0 14 14"><path d="M3 11 11 3M5 3h6v6" stroke="#fff" stroke-width="1.4" fill="none"/></svg></a><h3>The ULTIMATE Whole House Water Treatment System</h3></article>
  <article class="card"><div class="shot" role="img" aria-label="Smart water heater regulator display"></div><a class="go"><svg width="18" height="18" viewBox="0 0 14 14"><path d="M3 11 11 3M5 3h6v6" stroke="#fff" stroke-width="1.4" fill="none"/></svg></a><h3>Smart Water Heater Regulator with Automated Stand-By for Power Savings</h3></article>
  <article class="card"><div class="shot" role="img" aria-label="Pressure booster pump with gauge"></div><a class="go"><svg width="18" height="18" viewBox="0 0 14 14"><path d="M3 11 11 3M5 3h6v6" stroke="#fff" stroke-width="1.4" fill="none"/></svg></a><h3>Whole House Water Pressure Booster</h3></article>
  <article class="card"><div class="shot" role="img" aria-label="Expansion tank on copper pipe"></div><a class="go"><svg width="18" height="18" viewBox="0 0 14 14"><path d="M3 11 11 3M5 3h6v6" stroke="#fff" stroke-width="1.4" fill="none"/></svg></a><h3>Hot Water Heater Tank Volume Booster</h3></article>
  <article class="card"><div class="shot" role="img" aria-label="Leak detector and shutoff valve"></div><a class="go"><svg width="18" height="18" viewBox="0 0 14 14"><path d="M3 11 11 3M5 3h6v6" stroke="#fff" stroke-width="1.4" fill="none"/></svg></a><h3>Leak Detector with Automatic Water Shutoff</h3></article>
  <article class="card"><div class="shot" role="img" aria-label="UV air purifier unit with glowing lamp"></div><a class="go"><svg width="18" height="18" viewBox="0 0 14 14"><path d="M3 11 11 3M5 3h6v6" stroke="#fff" stroke-width="1.4" fill="none"/></svg></a><h3>Whole House UV Air Purification System</h3></article>
  <article class="card"><div class="shot" role="img" aria-label="Leak alarm sensors with phone app"></div><a class="go"><svg width="18" height="18" viewBox="0 0 14 14"><path d="M3 11 11 3M5 3h6v6" stroke="#fff" stroke-width="1.4" fill="none"/></svg></a><h3>Multi-Gas Detector for Carbon Monoxide, Natural Gas, Propane, Methane...</h3></article>
</div>
<article class="card wide"><div class="shot" role="img" aria-label="Handheld multi-gas detector"></div><a class="go"><svg width="18" height="18" viewBox="0 0 14 14"><path d="M3 11 11 3M5 3h6v6" stroke="#fff" stroke-width="1.4" fill="none"/></svg></a><h3>Multi-Gas Detector for Carbon Monoxide, Natural Gas, Propane, Methane, Explosive Gasses, Smoke &amp; Fire</h3></article>
<footer>
  <div class="f-brand"><span class="dot"></span>Mr. Clear Brook</div>
  <p class="f-about">Delivering premium water treatment, water heating and safety solutions for healthier homes and smarter living.</p>
  <div class="socials"><i></i><i></i><i></i></div>
  <div class="col" style="left:622px"><h4>Quick Links</h4><ul><li>Home</li><li>Products</li><li>About Us</li><li>Resources</li><li>Contact Us</li></ul></div>
  <div class="col" style="left:788px"><h4>Support</h4><ul><li>FAQs</li><li>Product Manuals</li><li>Warranty</li><li>Returns</li><li>Contact Support</li></ul></div>
  <div class="col" style="left:925px"><h4>Contact Us</h4><ul>
    <li><svg width="13" height="13" viewBox="0 0 24 24"><path d="M12 2a7 7 0 0 0-7 7c0 5 7 13 7 13s7-8 7-13a7 7 0 0 0-7-7zm0 9.5A2.5 2.5 0 1 1 12 6.5a2.5 2.5 0 0 1 0 5z" fill="none" stroke="#3da0ff" stroke-width="2"/></svg>Lakeview, CA 90000, USA</li>
    <li><svg width="13" height="13" viewBox="0 0 24 24"><path d="M6.6 10.8a15 15 0 0 0 6.6 6.6l2.2-2.2c.3-.3.7-.4 1-.2 1.1.4 2.3.6 3.6.6.6 0 1 .4 1 1V20c0 .6-.4 1-1 1A17 17 0 0 1 3 4c0-.6.4-1 1-1h3.5c.6 0 1 .4 1 1 0 1.3.2 2.5.6 3.6.1.3 0 .7-.2 1z" fill="none" stroke="#3da0ff" stroke-width="2"/></svg>(800) 555-0142</li>
    <li><svg width="13" height="13" viewBox="0 0 24 24"><path d="M3 5h18v14H3zM3 6l9 6 9-6" fill="none" stroke="#3da0ff" stroke-width="2"/></svg>info@mrbrookly.example</li></ul></div>
  <div class="bottom">© 2025 Mr. Clear Brook Treatment Systems &amp; Mr. Hot Kettle. All Rights Reserved.</div>
</footer>
</body>
</html>
```